New young doctors office business card

Doctor's office
Hello:
My name is Dr. Mateo Anselmo Quiroga Benítez. I need a business card for my new office located within a hospital. The name of the hospital is "Hospital Almendral". Although the hospital logo and name must be included in the business card, please make me a personal logo for myself. The logo might be maybe my name in a stylish font, or my initials (MAQB) or something like that. Im more inclined to a font logo, rather than a image logo, but a good one might change my mind. The info on my business card is going to be in spanish. The following info must be included please (the info within parenthesis is not to be included, it is provided for you to understand it since it's in spanish, so you can properly place it on the card):
-Dr. Mateo Anselmo Quiroga Benítez (my name)
-Medicina general (My specialty)
-Hospital Almendral (The name of the hospital where my office is)
-Calle Tomás Ibarrola #527 Col. Peñascal (address)
-Tel 471-5836 (Office phone)
-Sábado y domingo 10:00 am a 10:00pm (Office hours)
-Emergencias: 613-907-5148 (Emergency phone)
-mateoqb@correoandino.net (email)
-English Spoken
So, that's all the info i need to be on the business card. Although it's a business card for a doctor's office, i dont want it to be a boring, plain business card. Make it eye-catchy and stylish please. As i said, the hospital logo must be included. You'll find it on the heading of the PDF file i attached, but dont make it the center of attention.
Physician
Hello:My name is Dr. Mateo Anselmo Quiroga Benítez. I need a business card for my new office located within a hospital. The name of the hospital is "Hospital Almendral". Although the hospital logo and name must be included in the business card, please make me a personal logo for myself. The logo might be maybe my name in a stylish font, or my initials (MAQB) or something like that. Im more inclined to a font logo, rather than a image logo, but a good one might change my mind. The info on my business card is going to be in spanish. The following info must be included please (the info within parenthesis is not to be included, it is provided for you to understand it since it's in spanish, so you can properly place it on the card):-Dr. Mateo Anselmo Quiroga Benítez (my name)-Medicina general (My specialty)-Hospital Almendral (The name of the hospital where my office is)-Calle Tomás Ibarrola #527 Col. Peñascal (address)-Tel 471-5836 (Office phone)-Sábado y domingo 10:00 am a 10:00pm (Office hours)-Emergencias: 613-907-5148 (Emergency phone)-mateoqb@correoandino.net (email)-English Spoken So, that's all the info i need to be on the business card. Although it's a business card for a doctor's office, i dont want it to be a boring, plain business card. Make it eye-catchy and stylish please. As i said, the hospital logo must be included. You'll find it on the heading of the PDF file i attached, but dont make it the center of attention.

```html
<!DOCTYPE html>
<html lang="es">
<head>
<meta charset="utf-8">
<title>Tarjeta de presentación – Dr. Mateo Anselmo Quiroga Benítez</title>
<link href="https://fonts.googleapis.com/css2?family=Montserrat:wght@400;500;700;800&display=swap" rel="stylesheet">
<style>
  :root {
    --bg: #d9d9d9;
    --card-dark: #0b0b0b;
    --card-light: #ffffff;
    --ink: #1a1a1a;
    --red: #c8102e;
    --red-dark: #9e1020;
    --purple: #8a3fb0;
    --violet: #5a2ea6;
    --green: #8cc63f;
    --navy: #2d3f8f;
    --ghost-dark: #1c1c1c;
    --ghost-light: #ececec;
  }
  * { box-sizing: border-box; margin: 0; padding: 0; }
  html, body { width: 1200px; height: 900px; overflow: hidden; }
  body {
    background: var(--bg);
    font-family: "Montserrat", Arial, sans-serif;
    position: relative;
  }
  .card {
    position: absolute;
    left: 250px;
    width: 700px;
    height: 400px;
    overflow: hidden;
    box-shadow: 0 8px 24px rgba(0,0,0,.25);
  }
  .card--front { top: 35px; background: var(--card-dark); }
  .card--back { top: 465px; background: var(--card-light); }

  .ghost-mark {
    position: absolute;
    font-weight: 800;
    font-size: 190px;
    letter-spacing: -6px;
    line-height: 1;
  }
  .card--front .ghost-mark { right: -40px; top: 20px; color: var(--ghost-dark); }
  .card--back .ghost-mark { right: -30px; top: -20px; color: var(--ghost-light); }

  .monogram {
    display: flex;
    align-items: center;
    gap: 12px;
  }
  .monogram__dot {
    width: 26px; height: 26px; border-radius: 50%;
    background: var(--green);
  }
  .monogram__name {
    font-weight: 800;
    color: var(--red);
    letter-spacing: 2px;
  }

  /* front */
  .front-identity {
    position: absolute;
    left: 0; right: 0; top: 120px;
    display: flex; flex-direction: column; align-items: center;
  }
  .front-identity .monogram__name { font-size: 62px; }
  .front-identity .doctor-name {
    margin-top: 18px;
    color: #fff; font-weight: 700; font-size: 21px; letter-spacing: .5px;
    text-transform: uppercase;
  }
  .front-identity .specialty {
    margin-top: 6px; color: var(--red); font-weight: 700; font-size: 15px;
    text-transform: uppercase; letter-spacing: 1px;
  }

  /* back */
  .back-identity { position: absolute; left: 36px; top: 44px; }
  .back-identity .monogram__name { font-size: 52px; }
  .back-identity .doctor-name {
    margin-top: 10px; color: var(--ink); font-weight: 700; font-size: 17px;
    text-transform: uppercase; letter-spacing: .3px;
  }
  .back-identity .specialty {
    margin-top: 2px; color: var(--red); font-weight: 700; font-size: 14px;
    text-transform: uppercase; letter-spacing: 1px;
  }
  .rule-main {
    position: absolute; left: 36px; top: 200px; width: 628px; height: 1.5px; background: var(--ink);
  }
  .hospital {
    position: absolute; right: 36px; top: 150px; text-align: right;
  }
  .hospital__name { font-weight: 700; font-size: 16px; color: var(--ink); }
  .hospital__address { font-size: 13px; color: var(--ink); margin-top: 3px; }
  .hospital-mark {
    position: absolute; right: 36px; top: 218px;
    display: flex; align-items: center; gap: 8px;
  }
  .hospital-mark__square { width: 22px; height: 22px; background: var(--navy); }
  .hospital-mark__name { font-weight: 800; font-size: 22px; color: var(--navy); }

  .contact {
    position: absolute; left: 36px; top: 226px;
    border-top: 1.5px solid var(--ink); padding-top: 10px; width: 300px;
    list-style: none;
  }
  .contact li {
    display: flex; align-items: center; gap: 10px;
    font-size: 15px; color: var(--ink); line-height: 25px;
  }
  .contact strong { font-weight: 700; }
  .contact svg { width: 18px; height: 18px; flex: none; }

  .footer-band { position: absolute; left: 0; right: 0; bottom: 0; height: 44px; }
  .footer-band svg { position: absolute; inset: 0; width: 100%; height: 100%; }
  .footer-band__english, .footer-band__hours {
    position: absolute; bottom: 12px; color: #fff; font-size: 15px; letter-spacing: 1px;
    text-transform: uppercase; font-weight: 500;
  }
  .footer-band__english { left: 36px; }
  .footer-band__hours { right: 36px; }
</style>
</head>
<body>

<section class="card card--front" aria-label="Frente de la tarjeta">
  <div class="ghost-mark" aria-hidden="true">MAQB</div>
  <div class="front-identity">
    <div class="monogram">
      <span class="monogram__name">MAQB</span>
      <span class="monogram__dot"></span>
    </div>
    <p class="doctor-name">Dr. Mateo Anselmo Quiroga Benítez</p>
    <p class="specialty">Medicina General</p>
  </div>
</section>

<section class="card card--back" aria-label="Reverso de la tarjeta">
  <div class="ghost-mark" aria-hidden="true">MAQB</div>

  <div class="back-identity">
    <div class="monogram">
      <span class="monogram__name">MAQB</span>
      <span class="monogram__dot"></span>
    </div>
    <p class="doctor-name">Dr. Mateo Anselmo Quiroga Benítez</p>
    <p class="specialty">Medicina General</p>
  </div>

  <div class="hospital">
    <p class="hospital__name">Hospital Almendral</p>
    <p class="hospital__address">Calle Tomás Ibarrola #527 Col. Peñascal</p>
  </div>
  <div class="hospital-mark">
    <span class="hospital-mark__square"></span>
    <span class="hospital-mark__name">Almendral</span>
  </div>

  <ul class="contact">
    <li>
      <svg viewBox="0 0 20 20" aria-hidden="true"><path fill="var(--red)" d="M2 7c0-3 4-4 8-4s8 1 8 4v2h-4V7H6v2H2zM5 10h10l2 7H3z"/><circle cx="10" cy="13.5" r="2" fill="#fff"/></svg>
      <span>Office: 471-5836</span>
    </li>
    <li>
      <svg viewBox="0 0 20 20" aria-hidden="true"><path fill="var(--red)" d="M2 7c0-3 4-4 8-4s8 1 8 4v2h-4V7H6v2H2zM5 10h10l2 7H3z"/><circle cx="10" cy="13.5" r="2" fill="#fff"/></svg>
      <span><strong>Emergencias: 613-907-5148</strong></span>
    </li>
    <li>
      <svg viewBox="0 0 20 20" aria-hidden="true"><rect x="1" y="4" width="18" height="12" fill="var(--red)"/><path d="M1 4l9 7 9-7" fill="none" stroke="#fff" stroke-width="1.5"/></svg>
      <span>mateoqb@correoandino.net</span>
    </li>
  </ul>

  <div class="footer-band">
    <svg viewBox="0 0 700 44" preserveAspectRatio="none" aria-hidden="true">
      <defs>
        <linearGradient id="bandPurple" x1="0" x2="1">
          <stop offset="0" stop-color="var(--purple)"/>
          <stop offset="1" stop-color="var(--violet)"/>
        </linearGradient>
        <linearGradient id="bandRed" x1="0" x2="1">
          <stop offset="0" stop-color="var(--red-dark)"/>
          <stop offset="1" stop-color="var(--red)"/>
        </linearGradient>
      </defs>
      <rect x="0" y="14" width="300" height="30" fill="url(#bandPurple)"/>
      <polygon points="300,0 700,0 700,44 300,44" fill="url(#bandRed)"/>
      <polyline points="292,30 300,30 305,14 310,40 315,24 320,30 330,30" fill="none" stroke="#fff" stroke-width="1.5"/>
    </svg>
    <span class="footer-band__english">English Spoken</span>
    <span class="footer-band__hours">Sábado y Domingo 10:00 AM a 10:00PM</span>
  </div>
</section>

</body>
</html>
```